BrightLane Driving School

I need a Facebook page for my Driving School. I teach mostly teenagers how to drive in New Hampshire but also do private classes for adults as well. More info can be found at brightlanelessons.com

```html
<!DOCTYPE html>
<html lang="en">
<head>
<meta charset="utf-8">
<title>BrightLane Driving School – Facebook Cover</title>
<link rel="stylesheet" href="https://fonts.googleapis.com/css2?family=Anton&family=Poppins:wght@600;800&display=swap">
<style>
  :root {
    --asphalt: #1d1d1d;
    --asphalt-edge: #2b2b2b;
    --lane-yellow: #f5c40f;
    --lane-yellow-deep: #e8b400;
    --ink: #1a1a1a;
    --white: #ffffff;
    --page: #eeeeee;
    --dash: rgba(255,255,255,0.07);
  }
  * { margin: 0; padding: 0; box-sizing: border-box; }
  html, body {
    width: 1200px; height: 802px; overflow: hidden;
    background: var(--page);
  }
  .cover {
    position: absolute; left: 0; top: 88px;
    width: 1200px; height: 625px;
    background: var(--asphalt);
    overflow: hidden;
  }
  .edge-strip {
    position: absolute; left: 0; width: 100%; height: 23px;
    background: var(--asphalt-edge);
  }
  .edge-strip.top { top: 0; }
  .edge-strip.bottom { bottom: 0; height: 18px; }
  .lane-line {
    position: absolute; left: 0; width: 100%; height: 25px;
    background: var(--lane-yellow);
  }
  .lane-line.top { top: 23px; }
  .lane-line.bottom { top: 583px; }
  .road-dashes { position: absolute; inset: 0; }
  .tag {
    position: absolute; left: 71px;
    height: 46px;
    background: var(--lane-yellow);
    color: var(--ink);
    font: 800 21px/46px "Poppins", sans-serif;
    padding-left: 32px;
    letter-spacing: 0.2px;
    clip-path: polygon(1% 8%, 4% 0, 97% 4%, 100% 22%, 98% 50%, 100% 80%, 96% 100%, 3% 94%, 0 78%, 2% 50%, 0 24%);
  }
  .tag.teen { top: 90px; width: 531px; }
  .tag.adult { top: 146px; width: 456px; }
  .brand {
    position: absolute; left: 103px; top: 230px;
    display: flex; align-items: center; gap: 14px;
  }
  .brand-dot {
    width: 96px; height: 96px; border-radius: 50%;
    background: var(--lane-yellow);
    flex: none;
  }
  .brand-name {
    font: 800 30px/1.05 "Poppins", sans-serif;
    color: var(--white);
  }
  .brand-phone {
    margin-top: 8px;
    font: 800 15px/1 "Poppins", sans-serif;
    color: var(--white);
    letter-spacing: 1.5px;
  }
  .photo-pair { position: absolute; left: 560px; top: 77px; }
  .headline {
    position: absolute; right: 58px; top: 376px;
    text-align: right;
    font: 400 62px/1.12 "Anton", sans-serif;
    text-transform: uppercase;
    letter-spacing: 0.3px;
  }
  .headline .line-white { color: var(--white); display: block; }
  .headline .line-yellow { color: var(--lane-yellow); display: block; }
  .tagline {
    position: absolute; right: 65px; top: 525px;
    font: 600 17.5px/1 "Poppins", sans-serif;
    color: var(--lane-yellow);
  }
</style>
</head>
<body>
  <main class="cover">
    <div class="edge-strip top"></div>
    <div class="lane-line top"></div>

    <svg class="road-dashes" width="1200" height="625" viewBox="0 0 1200 625" aria-hidden="true">
      <g fill="var(--dash)">
        <rect x="0" y="0" width="80" height="32" transform="translate(485 322) rotate(-32)"/>
        <rect x="0" y="0" width="110" height="44" transform="translate(360 410) rotate(-32)"/>
        <rect x="0" y="0" width="130" height="52" transform="translate(240 510) rotate(-32)"/>
        <rect x="0" y="0" width="70" height="28" transform="translate(590 255) rotate(-32)"/>
      </g>
    </svg>

    <div class="tag teen">TEENAGE GROUP DRIVER EDUCATION</div>
    <div class="tag adult">PRIVATE CLASSES FOR ADULTS</div>

    <div class="brand">
      <div class="brand-dot"></div>
      <div>
        <div class="brand-name">BrightLane<br>Driving School</div>
        <div class="brand-phone">603 555 0142</div>
      </div>
    </div>

    <svg class="photo-pair" width="560" height="300" viewBox="0 0 560 300">
      <defs>
        <linearGradient id="lesson-tone" x1="0" y1="0" x2="1" y2="1">
          <stop offset="0" stop-color="#6e6a63"/>
          <stop offset="1" stop-color="#b7b1a6"/>
        </linearGradient>
        <linearGradient id="driver-tone" x1="0" y1="0" x2="1" y2="1">
          <stop offset="0" stop-color="#e2c24a"/>
          <stop offset="1" stop-color="#f2ece2"/>
        </linearGradient>
        <clipPath id="top-half"><rect x="0" y="0" width="560" height="146"/></clipPath>
      </defs>
      <circle cx="149" cy="149" r="147" fill="none" stroke="rgba(245,196,15,0.22)" stroke-width="4"/>
      <circle cx="149" cy="149" r="139" fill="var(--white)"/>
      <circle cx="149" cy="149" r="139" fill="var(--lane-yellow)" clip-path="url(#top-half)"/>
      <circle cx="408" cy="149" r="139" fill="var(--lane-yellow)"/>
      <circle cx="408" cy="149" r="124" fill="var(--white)"/>
      <circle cx="149" cy="149" r="118" fill="url(#lesson-tone)" role="img" aria-label="Photo of an instructor coaching a teenage student driver in the car"/>
      <circle cx="408" cy="149" r="118" fill="url(#driver-tone)" role="img" aria-label="Photo of a smiling adult driver leaning out of a yellow car window"/>
    </svg>

    <h1 class="headline">
      <span class="line-white">Preparing you for the</span>
      <span class="line-yellow">Road Driving School</span>
    </h1>
    <p class="tagline">Quality drivers education instruction with a new fleet of vehicles.</p>

    <div class="lane-line bottom"></div>
    <div class="edge-strip bottom"></div>
  </main>
</body>
</html>
```